Larkmoor Capital Partners need a desert themed website!

We need a web design and development for our informational website for our new company named Larkmoor Capital Partners. We would like it to be desert themed and it can be color or black and white. We would like it to be classy and clean, while also talking to the benefits of investment partner with us.

We're thinking probably a home page with a nice image of a Scottsdale landscape, then other pages would What we offer our partners page (or other wording if you find something better), a meet the founder page, and a contact us page.

What we offer our partners (or other wording if you think of something better):
Our investors offer an opportunity to families that cannot usually get approved for a mortgage, to be able to become future homeowners. Thus, Benefiting both the investors and local surrounding community members. Our investors get to both have all the benefits of an investment with receiving above market rates of return to themselves and helping families find homes at the same time.

Maybe also build an infographic with these benefits: Safety, Security, Long-term investment horizon, cashflow, tax benefits, above market rate of return, and capital growth.

And a meet the founder page. With my headshot.

Dale Corwith is a private equity investor providing significantly above market returns to his investment partners while taking the time to be involved with his community and family. Dale first honed his skills in taking calculated risk decisions while very young where he took on playing poker professionally. He succeeded at the highest levels for over a decade competing in high stakes professional cash games around the world.

From the poker world he transitioned to investing in public and private markets. He took an approach of knowing the companies he invests in intimately and after over 10,000 hours of research became known in his community as the person to get investment advice on the electric vehicle industry for his voracious research and expert insight.

He now invests in single family homes in the Phoenix market using his past experience analyzing probabilistic outcomes and comparing the ROIs of different potential strategies. These skills have contributed to his success in investing in companies where he used his ability to assess risk to reward ratios to significantly outperform the market over an extended period.

Contact page we want my email Dale@LarkmoorFunds.example, my instagram: @DaleCorwith, and my linkedin https://www.profilehub.example/in/dale-corwith-58172036/

I have included my headshot for the about me page. I've included some saguaro generated images feel free to incorporate into the website (or make them the company logo), or not, whatever you feel gives the best look for the website.

```html
<!DOCTYPE html>
<html lang="en">
<head>
<meta charset="utf-8">
<title>Larkmoor Capital Partners</title>
<link rel="stylesheet" href="https://fonts.googleapis.com/css2?family=Exo+2:wght@600;700;800&family=Open+Sans:wght@400;600;700&display=swap">
<style>
:root{
  --orange:#d9742b;
  --orange-dark:#c4621e;
  --ink:#2e2926;
  --brown:#7a5843;
  --beige:#ece5dd;
  --card:#e3dbd1;
  --cream:#faf6f2;
  --white:#ffffff;
  --muted:#5a524c;
  --line:#8f8780;
}
*{box-sizing:border-box;margin:0;padding:0}
html,body{width:1200px;height:3180px;overflow:hidden}
body{background:var(--white);color:var(--ink);font-family:"Open Sans",Arial,sans-serif;position:relative}
.heading{font-family:"Exo 2",Arial,sans-serif;font-weight:800;text-transform:uppercase;color:var(--ink);letter-spacing:.5px}
.btn{display:inline-block;background:var(--orange);color:var(--white);font-family:"Open Sans",Arial,sans-serif;font-weight:600;font-size:14px;padding:10px 22px;border-radius:2px;text-decoration:none}

/* Nav */
.site-nav{position:absolute;top:0;left:0;width:1200px;height:62px;background:var(--white);display:flex;align-items:center;padding:0 112px;z-index:2}
.brand{font-family:"Exo 2",Arial,sans-serif;color:var(--ink);line-height:1}
.brand-name{font-weight:800;font-size:24px;letter-spacing:.5px}
.brand-sub{font-weight:600;font-size:11px;letter-spacing:.8px;margin-top:3px}
.nav-links{display:flex;gap:28px;margin-left:auto;margin-right:40px;list-style:none;font-size:14px}
.nav-links a{color:var(--ink);text-decoration:none}
.nav-links .active{font-weight:600}
.nav-cta{padding:9px 20px}

/* Hero */
.hero{position:absolute;top:62px;left:0;width:1200px;height:450px;overflow:hidden}
.hero-scene{position:absolute;inset:0;background:
  linear-gradient(180deg,#f4ece4 0%,#efe2d4 35%,#e9b98d 58%,#d9803f 72%,#b85a26 86%,#9b4a21 100%)}
.hero-text{position:absolute;top:170px;left:0;width:100%;text-align:center}
.hero-kicker{font-family:"Exo 2",Arial,sans-serif;font-weight:700;font-size:28px;color:var(--ink);letter-spacing:1px}
.hero-title{font-size:60px;line-height:1.05;margin-top:8px}
.hero-wave{position:absolute;bottom:-1px;left:0}

/* Offer */
.offer{position:absolute;top:512px;left:0;width:1200px;height:520px;background:var(--white)}
.offer-copy{position:absolute;left:112px;top:72px;width:560px}
.offer-copy .heading{font-size:44px;line-height:1.1}
.offer-copy p{margin-top:24px;font-size:15px;line-height:1.85;color:var(--muted)}
.offer-copy .btn{margin-top:26px}
.offer-photo{position:absolute;left:724px;top:50px;width:364px;height:400px;border-radius:70px 0 0 0;background:linear-gradient(160deg,#dfe7ee 0%,#bcc8d3 45%,#6d7880 80%,#3f464c 100%)}

/* Benefits */
.benefits{position:absolute;top:1032px;left:0;width:1200px;height:610px;background:var(--beige)}
.benefits .heading{position:absolute;top:56px;width:100%;text-align:center;font-size:44px}
.benefit-chart{position:absolute;top:0;left:0}
.benefit-label{position:absolute;font-size:16px;font-weight:600;color:var(--ink);line-height:1.3}
.benefit-label.left{text-align:right}
.chart-center{position:absolute;left:480px;top:334px;width:240px;text-align:center;font-family:"Exo 2",Arial,sans-serif;color:var(--ink)}
.chart-center .c-name{font-weight:800;font-size:28px;line-height:1}
.chart-center .c-sub{font-weight:600;font-size:12px;letter-spacing:1px;margin-top:4px}

/* Founder */
.founder{position:absolute;top:1642px;left:0;width:1200px;height:572px;background:var(--cream)}
.founder-photo{position:absolute;left:112px;top:90px;width:368px;height:400px;border-radius:0 140px 0 0;background:linear-gradient(170deg,#d9d4cf 0%,#b9aca1 50%,#8d7a6c 100%)}
.founder-copy{position:absolute;left:600px;top:112px;width:490px}
.founder-copy .heading{font-size:44px;line-height:1.1}
.founder-copy p{margin-top:22px;font-size:14px;line-height:1.85;color:var(--muted)}
.founder-copy .btn{margin-top:24px}

/* Contact */
.contact{position:absolute;top:2214px;left:0;width:1200px;height:640px;background:var(--white)}
.contact .section-title{position:absolute;top:68px;width:100%;text-align:center;font-size:44px}
.contact-form{position:absolute;left:160px;top:176px;width:432px;height:420px;background:var(--card);padding:28px 50px;box-shadow:0 6px 18px rgba(0,0,0,.08)}
.contact-form h3{font-size:16px;font-weight:700;margin-bottom:18px}
.field{display:block;width:340px;height:38px;background:var(--white);border:none;margin-bottom:14px;padding:0 12px;font-size:13px;color:var(--muted);display:flex;align-items:center}
.field.message{height:108px;align-items:flex-start;padding-top:10px}
.contact-form .btn{margin-top:10px}
.contact-info{position:absolute;left:688px;top:204px;width:360px}
.contact-info h3{font-size:16px;font-weight:700;margin-bottom:22px}
.info-item{display:flex;gap:16px;margin-bottom:22px}
.info-item svg{flex:none;margin-top:2px}
.info-item .label{font-weight:700;font-size:14px;color:var(--orange);display:block}
.info-item .value{font-size:14px;line-height:1.6;color:var(--ink)}
.follow{display:flex;align-items:center;gap:12px;margin-top:30px;font-weight:700;font-size:16px}
.social-dot{width:30px;height:30px;border:2px solid var(--ink);border-radius:50%}

/* Footer */
.site-footer{position:absolute;top:2830px;left:0;width:1200px;height:350px}
.footer-wave{position:absolute;top:0;left:0}
.footer-body{position:absolute;top:80px;left:0;width:1200px;height:270px;background:var(--ink);text-align:center;color:var(--white)}
.footer-brand{margin-top:60px;font-family:"Exo 2",Arial,sans-serif;line-height:1}
.footer-brand .brand-name{font-weight:800;font-size:28px}
.footer-brand .brand-sub{font-weight:600;font-size:12px;letter-spacing:1px;margin-top:4px}
.footer-links{display:flex;justify-content:center;gap:28px;list-style:none;margin-top:26px;font-size:14px}
.footer-links a{color:var(--white);text-decoration:none}
.copyright{margin-top:18px;font-size:14px}
</style>
</head>
<body>

<header class="site-nav">
  <div class="brand">
    <div class="brand-name">LARKMOOR</div>
    <div class="brand-sub">CAPITAL PARTNERS</div>
  </div>
  <ul class="nav-links">
    <li><a class="active" href="#home">Home</a></li>
    <li><a href="#offer">What we offer</a></li>
    <li><a href="#founder">Meet the founder</a></li>
    <li><a href="#contact">Contact us</a></li>
  </ul>
  <a class="btn nav-cta" href="#contact">Get Started</a>
</header>

<section class="hero" id="home">
  <div class="hero-scene" role="img" aria-label="Desert landscape illustration with orange mesas and sand dunes under a pale sky"></div>
  <div class="hero-text">
    <div class="hero-kicker">WELCOME TO</div>
    <h1 class="heading hero-title">LARKMOOR<br>CAPITAL PARTNERS</h1>
  </div>
  <svg class="hero-wave" width="1200" height="70" viewBox="0 0 1200 70" aria-hidden="true">
    <path d="M0 30 C200 70 380 10 600 34 C820 58 1000 14 1200 36 L1200 70 L0 70 Z" fill="#ffffff"/>
  </svg>
</section>

<section class="offer" id="offer">
  <div class="offer-copy">
    <h2 class="heading">What we offer<br>our partners</h2>
    <p>Our investors offer an opportunity to families that cannot usually get approved for a mortgage, to be able to become future homeowners. Thus, Benefiting both the investors and local surrounding community members. Our investors get to both have all the benefits of an investment with receiving above market rates of return to themselves and helping families find homes at the same time.</p>
    <a class="btn" href="#offer">Learn More</a>
  </div>
  <div class="offer-photo" role="img" aria-label="Photo of an advisor meeting with an investment partner at an office desk"></div>
</section>

<section class="benefits">
  <h2 class="heading">Our Benefits</h2>
  <svg class="benefit-chart" width="1200" height="610" viewBox="0 0 1200 610" aria-hidden="true">
    <polygon points="600,166 765,261 765,451 600,546 435,451 435,261" fill="none" stroke="#9a928b" stroke-width="10" stroke-linejoin="round"/>
    <!-- top-left: tax -->
    <circle cx="518" cy="213" r="30" fill="#d9742b"/>
    <rect x="506" y="200" width="24" height="28" rx="2" fill="none" stroke="#fff" stroke-width="2.5"/>
    <line x1="511" y1="208" x2="525" y2="208" stroke="#fff" stroke-width="2"/>
    <line x1="511" y1="214" x2="525" y2="214" stroke="#fff" stroke-width="2"/>
    <line x1="511" y1="220" x2="521" y2="220" stroke="#fff" stroke-width="2"/>
    <!-- top-right: safety -->
    <circle cx="682" cy="213" r="30" fill="#2e2926"/>
    <path d="M682 198 L696 204 L696 214 C696 222 690 228 682 231 C674 228 668 222 668 214 L668 204 Z" fill="none" stroke="#fff" stroke-width="2.5"/>
    <path d="M676 214 L681 219 L689 209" fill="none" stroke="#fff" stroke-width="2.5"/>
    <!-- left: above market -->
    <circle cx="435" cy="356" r="30" fill="#7a5843"/>
    <polyline points="421,366 431,354 439,360 450,346" fill="none" stroke="#fff" stroke-width="2.5"/>
    <polyline points="443,346 450,346 450,353" fill="none" stroke="#fff" stroke-width="2.5"/>
    <!-- right: long term -->
    <circle cx="765" cy="356" r="30" fill="#d9742b"/>
    <circle cx="765" cy="356" r="13" fill="none" stroke="#fff" stroke-width="2.5"/>
    <polyline points="765,348 765,356 771,360" fill="none" stroke="#fff" stroke-width="2.5"/>
    <!-- bottom-left: capital growth -->
    <circle cx="518" cy="499" r="30" fill="#2e2926"/>
    <rect x="506" y="500" width="5" height="12" fill="#fff"/>
    <rect x="515" y="493" width="5" height="19" fill="#fff"/>
    <rect x="524" y="486" width="5" height="26" fill="#fff"/>
    <!-- bottom-right: cashflow -->
    <circle cx="682" cy="499" r="30" fill="#d9742b"/>
    <circle cx="682" cy="499" r="13" fill="none" stroke="#fff" stroke-width="2.5"/>
    <text x="682" y="505" text-anchor="middle" font-family="Open Sans, Arial, sans-serif" font-size="16" font-weight="700" fill="#fff">$</text>
  </svg>
  <div class="chart-center">
    <div class="c-name">LARKMOOR</div>
    <div class="c-sub">CAPITAL PARTNERS</div>
  </div>
  <div class="benefit-label left" style="right:712px;top:202px">Tax benefits</div>
  <div class="benefit-label" style="left:736px;top:202px">Safety and Security</div>
  <div class="benefit-label left" style="right:796px;top:334px;width:180px">Above market rate<br>of return</div>
  <div class="benefit-label" style="left:820px;top:334px;width:190px">Long-term investment<br>horizon</div>
  <div class="benefit-label left" style="right:712px;top:488px">Capital growth</div>
  <div class="benefit-label" style="left:736px;top:488px">Cashflow</div>
</section>

<section class="founder" id="founder">
  <div class="founder-photo" role="img" aria-label="Headshot of founder Dale Corwith"></div>
  <div class="founder-copy">
    <h2 class="heading">Meet the<br>Founder</h2>
    <p>Dale Corwith is a private equity investor providing significantly above market returns to his investment partners while taking the time to be involved with his community and family. Dale first honed his skills in taking calculated risk decisions while very young where he took on playing poker professionally. He succeeded at the highest levels for over a decade competing in high-stakes professional cash games around the world.</p>
    <a class="btn" href="#founder">Learn More</a>
  </div>
</section>

<section class="contact" id="contact">
  <h2 class="heading section-title">Contact Us</h2>
  <form class="contact-form">
    <h3>Fill the form</h3>
    <div class="field">Name</div>
    <div class="field">Phone</div>
    <div class="field">Email Address</div>
    <div class="field message">Message</div>
    <span class="btn">Learn More</span>
  </form>
  <div class="contact-info">
    <h3>Contact information</h3>
    <div class="info-item">
      <svg width="20" height="22" viewBox="0 0 20 22" aria-hidden="true"><path d="M10 1 C5 1 2 5 2 9 C2 14 10 21 10 21 C10 21 18 14 18 9 C18 5 15 1 10 1 Z" fill="none" stroke="#d9742b" stroke-width="2"/><circle cx="10" cy="9" r="3" fill="#d9742b"/></svg>
      <div><span class="label">Address:</span><span class="value">Larkmoor Capital Partners'<br>Address comes here</span></div>
    </div>
    <div class="info-item">
      <svg width="20" height="20" viewBox="0 0 20 20" aria-hidden="true"><path d="M4 2 L8 2 L9 6 L7 8 C8 11 9 12 12 13 L14 11 L18 12 L18 16 C18 17 17 18 16 18 C8 18 2 12 2 4 C2 3 3 2 4 2 Z" fill="none" stroke="#d9742b" stroke-width="2"/></svg>
      <div><span class="label">Main Number:</span><span class="value">+1 555-014-2280</span></div>
    </div>
    <div class="info-item">
      <svg width="20" height="16" viewBox="0 0 20 16" aria-hidden="true"><rect x="1" y="1" width="18" height="14" rx="1" fill="none" stroke="#d9742b" stroke-width="2"/><polyline points="1,2 10,9 19,2" fill="none" stroke="#d9742b" stroke-width="2"/></svg>
      <div><span class="label">Email:</span><span class="value">Dale@LarkmoorFunds.example</span></div>
    </div>
    <div class="follow">Follow Us: <span class="social-dot" aria-label="Profile link"></span><span class="social-dot" aria-label="Photo profile link"></span></div>
  </div>
</section>

<footer class="site-footer">
  <svg class="footer-wave" width="1200" height="82" viewBox="0 0 1200 82" aria-hidden="true">
    <path d="M0 40 C180 10 360 60 600 36 C840 12 1020 60 1200 30 L1200 82 L0 82 Z" fill="#2e2926"/>
  </svg>
  <div class="footer-body">
    <div class="footer-brand">
      <div class="brand-name">LARKMOOR</div>
      <div class="brand-sub">CAPITAL PARTNERS</div>
    </div>
    <ul class="footer-links">
      <li><a href="#home">Home</a></li>
      <li><a href="#offer">What we offer</a></li>
      <li><a href="#founder">Meet the founder</a></li>
      <li><a href="#contact">Contact us</a></li>
    </ul>
    <p class="copyright">2024 Larkmoor Capital Partners. All Rights Reserved.</p>
  </div>
</footer>

</body>
</html>
```